Brivane - Business Cards for a new venture

create business card for a startup classified business dealing in construction materials, the cards need to have a professional look but modern, more serious than playful, one of the samples must include the official font (attached), please explore using the official colors in the company's logo

Target Market(s)

Energy sector

Contact Information for Business Card

Font styles to use
Other font styles liked:
• suissnord

Requirements
Must have
• corporate colors (in logo attached)
Nice to have
• Official font (in one of the samples) font is : suissnord
Should not have
• Cartoonish look

```html
<!DOCTYPE html>
<html lang="en">
<head>
<meta charset="utf-8">
<title>Brivane – Business Cards</title>
<link rel="stylesheet" href="https://fonts.googleapis.com/css2?family=Orbitron:wght@400;500&display=swap">
<style>
  :root {
    --navy: #1d4587;
    --steel: #8e8f94;
    --paper: #ffffff;
    --backdrop: #e9e9eb;
    --shadow: rgba(20, 30, 50, 0.14);
  }
  * { box-sizing: border-box; margin: 0; padding: 0; }
  html, body {
    width: 1200px; height: 1200px; overflow: hidden;
    background: var(--backdrop);
    font-family: "Orbitron", "Arial", sans-serif;
  }
  .sheet {
    width: 1200px; height: 1200px;
    display: flex; flex-direction: column; align-items: center; justify-content: center;
    gap: 60px;
  }
  .card {
    position: relative;
    width: 840px; height: 480px;
    background: var(--paper);
    box-shadow: 0 10px 30px var(--shadow);
  }

  /* Front */
  .card--front {
    display: flex; align-items: center; justify-content: center;
  }
  .brand {
    display: flex; align-items: center; gap: 22px;
  }
  .brand__mark {
    width: 30px; height: 30px; background: var(--navy);
  }
  .brand__name {
    color: var(--steel);
    font-weight: 400;
    text-transform: uppercase;
    letter-spacing: 0.12em;
  }
  .card--front .brand__name { font-size: 72px; }

  /* Back */
  .card--back { display: flex; }
  .card__identity {
    width: 45%;
    display: flex; align-items: center; justify-content: center;
  }
  .card--back .brand { gap: 14px; }
  .card--back .brand__mark { width: 18px; height: 18px; }
  .card--back .brand__name { font-size: 38px; }
  .card__divider {
    width: 3px; background: var(--navy);
    margin: 70px 0;
  }
  .card__details {
    flex: 1;
    padding: 92px 0 0 44px;
    color: var(--navy);
  }
  .person__name {
    font-size: 30px; font-weight: 500; letter-spacing: 0.02em;
  }
  .person__name .surname { color: var(--steel); }
  .person__role {
    font-size: 19px; margin-top: 6px; letter-spacing: 0.03em;
  }
  .contact { list-style: none; margin-top: 26px; }
  .contact__item {
    display: flex; align-items: center; gap: 16px;
    font-size: 22px; font-weight: 500; margin-bottom: 10px;
  }
  .contact__icon { width: 24px; height: 24px; flex: none; }
  .address {
    font-style: normal; font-size: 14px; line-height: 1.6;
    margin-top: 20px; text-transform: uppercase; letter-spacing: 0.02em;
  }
</style>
</head>
<body>
<main class="sheet">

  <section class="card card--front" aria-label="Business card front">
    <div class="brand">
      <span class="brand__mark" aria-hidden="true"></span>
      <span class="brand__name">Brivane</span>
    </div>
  </section>

  <section class="card card--back" aria-label="Business card back">
    <div class="card__identity">
      <div class="brand">
        <span class="brand__mark" aria-hidden="true"></span>
        <span class="brand__name">Brivane</span>
      </div>
    </div>
    <div class="card__divider" aria-hidden="true"></div>
    <div class="card__details">
      <h1 class="person__name">Name of <span class="surname">Person</span></h1>
      <p class="person__role">Designation</p>
      <ul class="contact">
        <li class="contact__item">
          <svg class="contact__icon" viewBox="0 0 24 24" aria-hidden="true">
            <path fill="var(--navy)" d="M3 8c0-2 4-4 9-4s9 2 9 4v2h-5V8H8v2H3zM7 11h10l3 8H4z"/>
            <circle cx="12" cy="15" r="2" fill="#fff"/>
          </svg>
          +123 456 789
        </li>
        <li class="contact__item">
          <svg class="contact__icon" viewBox="0 0 24 24" aria-hidden="true">
            <circle cx="12" cy="12" r="10" fill="none" stroke="var(--navy)" stroke-width="2"/>
            <path fill="var(--navy)" d="M9 6l2 3-1.5 1.5c.6 1.6 1.8 2.8 3.5 3.5L14.5 12.5l3 2-1.5 2.5c-4 0-8.5-4.5-8.5-8.5z"/>
          </svg>
          +123 456 789
        </li>
        <li class="contact__item">
          <svg class="contact__icon" viewBox="0 0 24 24" aria-hidden="true">
            <rect x="2" y="5" width="20" height="14" fill="var(--navy)"/>
            <path d="M2 5l10 8 10-8" fill="none" stroke="#fff" stroke-width="1.6"/>
          </svg>
          name@email.com
        </li>
      </ul>
      <address class="address">
        No.01, Adrs Line 01,<br>
        Adrs Line 02, City, Country.
      </address>
    </div>
  </section>

</main>
</body>
</html>
```